we need a business card. We are an online company that provides work life balance services to our members. our website can be viewed at www.qorvenly.com.au
Our company logo is attached as well as a business card look that i like.

```html
<!DOCTYPE html>
<html lang="en">
<head>
<meta charset="utf-8">
<title>Qorvenly – Business Card</title>
<link rel="stylesheet" href="https://fonts.googleapis.com/css2?family=Questrial&display=swap">
<style>
  :root {
    --page-bg: #ecebe6;
    --card-white: #ffffff;
    --card-shadow: rgba(40, 50, 30, 0.18);
    --brand-green: #6db52e;
    --brand-green-light: #8cc63f;
    --brand-green-dark: #2f6d12;
    --brand-green-deep: #24560c;
    --text-on-green: #ffffff;
    --ornament-tone: #3d7f1a;
  }
  * { margin: 0; padding: 0; box-sizing: border-box; }
  html, body {
    width: 1200px;
    height: 900px;
    overflow: hidden;
    background: var(--page-bg);
    font-family: "Questrial", sans-serif;
  }
  .canvas {
    width: 1200px;
    height: 900px;
    display: flex;
    flex-direction: column;
    align-items: center;
    justify-content: center;
    gap: 40px;
  }
  .card {
    position: relative;
    width: 656px;
    height: 400px;
    border-radius: 4px;
    overflow: hidden;
    box-shadow: 0 10px 28px var(--card-shadow);
  }

  /* Front */
  .card-front { background: var(--card-white); }
  .brand {
    position: absolute;
    left: 44px;
    top: 176px;
    display: flex;
    align-items: center;
    gap: 14px;
  }
  .brand-dot {
    width: 34px;
    height: 34px;
    border-radius: 50%;
    background: var(--brand-green-light);
  }
  .brand-name {
    font-size: 40px;
    letter-spacing: 0.5px;
    color: var(--brand-green);
  }
  .contact-band {
    position: absolute;
    right: 0;
    bottom: 0;
    width: 420px;
    height: 132px;
    border-radius: 10px 0 0 0;
    background: linear-gradient(180deg, var(--brand-green-light), var(--brand-green));
    padding: 20px 18px 20px 22px;
    display: flex;
    flex-direction: column;
    justify-content: center;
    gap: 8px;
    color: var(--text-on-green);
    font-size: 12px;
    font-variant: small-caps;
    letter-spacing: 0.2px;
  }
  .contact-line { white-space: nowrap; }

  /* Back */
  .card-back {
    background: radial-gradient(circle at 60% 50%, var(--brand-green), var(--brand-green-dark) 70%, var(--brand-green-deep));
  }
  .back-ornament {
    position: absolute;
    left: 0;
    top: 0;
    width: 300px;
    height: 220px;
    background: radial-gradient(ellipse at 20% 25%, var(--ornament-tone), transparent 70%);
    opacity: 0.7;
  }
  .back-brand {
    position: absolute;
    right: 36px;
    bottom: 30px;
    font-size: 26px;
    color: var(--brand-green-light);
  }
</style>
</head>
<body>
  <main class="canvas">
    <section class="card card-front" aria-label="Business card front">
      <div class="brand">
        <span class="brand-dot"></span>
        <span class="brand-name">qorvenly</span>
      </div>
      <div class="contact-band">
        <p class="contact-line">Phone: 02 5550 1842 , Fax: 02 5550 1843</p>
        <p class="contact-line">Email: info@qorvenly.com.au</p>
        <p class="contact-line">Web: www.qorvenly.com.au</p>
        <p class="contact-line">Address: First Floor, 48 Bay View Road Lavender Bay 2060</p>
      </div>
    </section>

    <section class="card card-back" aria-label="Business card back">
      <div class="back-ornament" role="img" aria-label="Subtle tone-on-tone floral swirl ornament"></div>
      <span class="back-brand">qorvenly</span>
    </section>
  </main>
</body>
</html>
```